BRAMWELL Sofa Shop - Hipster Hero Header Design

I want to use the 'Meridale' theme on Storvik

https://meridale-theme-basic.storvikshop.example/
https://themes.storvikshop.example/themes/meridale/styles/plenwise/preview

The main, PRIMARY thing that I need designed is the top hero header to be customized to my shop. Please use the attached examples as a reference. I welcome creativity. I do like the hipster vibe. I'd like a sofa/Living Room theme.

****To be clear...I want a hipster header designed...I love the creative fonts on a filtered relevant photo*** I have placed attachments. Hipster fonts or a Badge, or some combo. If you need guidance please look at examples.

Words on design should be:

BRAMWELL SOFA SHOP.

(I will separately handle the functionality of the site.)
Thanks.
Updates

Please check my brief as I have streamlined my desires. I simply want a hero header designed and 3 buttons designed. Examples of hero headers are attached. Thanks. Added Saturday, September 26, 2015

Target Market(s)

Sofa Shoppers

Industry/Entity Type

Furniture Store

Number of Pages Required

1 page

Requirements
Nice to have
• Bramwell Sofa Shop
• https://meridale-theme-basic.storvikshop.example/

```html
<!DOCTYPE html>
<html lang="en">
<head>
<meta charset="utf-8">
<title>Bramwell Sofa Shop</title>
<link href="https://fonts.googleapis.com/css2?family=Playfair+Display:ital,wght@0,400;1,400&family=Raleway:wght@300;400;500;600&display=swap" rel="stylesheet">
<style>
  :root {
    --ink: #3d3d3d;
    --muted: #8f8f8f;
    --accent: #7ec3d6;
    --accent-pale: #a9d9e6;
    --white: #ffffff;
    --white-soft: rgba(255,255,255,0.7);
    --hero-dark: #1c1c1e;
    --hero-mid: #4a4a4e;
    --footer-bg: #dcc6bc;
    --footer-ink: #5a4a44;
    --card-line: #e6e6e6;
  }
  * { margin: 0; padding: 0; box-sizing: border-box; }
  html, body { width: 735px; height: 1200px; overflow: hidden; background: var(--white); }
  body { position: relative; font-family: "Raleway", Arial, sans-serif; color: var(--ink); }

  /* Hero */
  .hero { position: absolute; left: 0; top: 0; width: 735px; height: 392px; overflow: hidden; }
  .hero-photo { position: absolute; inset: 0;
    background: radial-gradient(ellipse at 50% 25%, #6a6a70 0%, var(--hero-mid) 30%, #2a2a2d 65%, var(--hero-dark) 100%); }
  .hero-tools { position: absolute; top: 20px; right: 20px; display: flex; gap: 12px; }
  .hero-content { position: absolute; left: 0; top: 118px; width: 735px; text-align: center; color: var(--white); }
  .hero-tagline { display: flex; align-items: center; justify-content: center; gap: 14px;
    font-family: "Playfair Display", Georgia, serif; font-style: italic; font-size: 16px; letter-spacing: 1px; }
  .hero-rule { display: block; width: 56px; height: 1px; background: var(--white-soft); }
  .brand-name { font-family: "Raleway", Arial, sans-serif; font-weight: 300; font-size: 64px;
    line-height: 1; margin-top: 14px; letter-spacing: 10px; text-transform: uppercase; padding-left: 10px; }
  .brand-sub { display: flex; align-items: center; justify-content: center; gap: 12px; margin-top: 14px;
    font-weight: 400; font-size: 18px; letter-spacing: 4px; }
  .brand-sub .hero-rule { width: 90px; }
  .hero-actions { margin-top: 22px; display: flex; flex-direction: column; align-items: center; gap: 8px; }
  .btn-pale { display: block; width: 116px; height: 12px; background: var(--accent-pale); border-radius: 6px;
    font-size: 8px; line-height: 12px; color: var(--white); letter-spacing: 1px; }
  .btn-outline { display: block; width: 84px; height: 16px; border: 1px solid var(--white);
    font-size: 8px; line-height: 14px; letter-spacing: 1.5px; text-transform: uppercase; }
  .hero-down { position: absolute; right: 18px; bottom: 14px; }

  /* Section headings */
  .section-title { position: absolute; left: 0; width: 735px; text-align: center;
    font-weight: 400; letter-spacing: 2px; color: var(--ink); }
  .section-title::before, .section-title::after { content: ""; display: block; width: 40px; height: 1px;
    background: var(--muted); margin: 0 auto; }
  .section-title::before { margin-bottom: 8px; }
  .section-title::after { margin-top: 8px; }
  .services-title { top: 410px; font-size: 26px; }
  .products-title { top: 678px; font-size: 19px; letter-spacing: 1px; }

  /* Services */
  .services { position: absolute; top: 488px; left: 0; width: 735px; display: flex; justify-content: center; gap: 78px; }
  .service { width: 110px; text-align: center; }
  .service-icon { width: 80px; height: 80px; margin: 0 auto; }
  .service-text { margin-top: 12px; font-size: 9px; line-height: 1.4; color: var(--muted); }

  /* Products */
  .products { position: absolute; top: 758px; left: 44px; width: 654px; display: flex; justify-content: space-between; }
  .product { width: 130px; height: 210px; border: 1px solid var(--card-line); background: var(--white);
    box-shadow: 0 1px 3px rgba(0,0,0,0.08); }
  .product-photo { width: 128px; height: 166px; }
  .photo-a { background: linear-gradient(180deg, #f1f1ef 0%, #e8e6e1 70%, #d9d4cc 100%); }
  .photo-b { background: linear-gradient(180deg, #d6d8da 0%, #bfc2c4 60%, #5c5f62 100%); }
  .photo-c { background: linear-gradient(180deg, #f4f3f0 0%, #dcdad6 60%, #9a9791 100%); }
  .photo-d { background: linear-gradient(180deg, #b7aea3 0%, #9c948b 55%, #7f7770 100%); }
  .product-info { display: flex; justify-content: space-between; padding: 10px 8px 0; font-size: 8px; }
  .product-name { color: var(--ink); }
  .product-price { color: var(--accent); font-weight: 600; }
  .view-all { position: absolute; top: 998px; left: 308px; width: 120px; height: 14px; border-radius: 7px;
    background: var(--accent-pale); color: var(--white); font-size: 8px; line-height: 14px; text-align: center; letter-spacing: 1px; }

  /* Footer */
  .site-footer { position: absolute; left: 0; top: 1040px; width: 735px; height: 160px; background: var(--footer-bg); color: var(--footer-ink); }
  .footer-cols { position: absolute; top: 24px; left: 159px; display: flex; gap: 56px; }
  .footer-col h4 { font-size: 9px; font-weight: 600; margin-bottom: 6px; }
  .footer-col li { list-style: none; font-size: 7px; line-height: 12px; display: flex; align-items: center; gap: 4px; }
  .dot { width: 7px; height: 7px; border-radius: 50%; background: var(--footer-ink); opacity: 0.6; }
  .newsletter { position: absolute; left: 159px; top: 96px; }
  .newsletter h4 { font-size: 8px; font-weight: 600; margin-bottom: 4px; }
  .newsletter-field { display: flex; }
  .newsletter-input { width: 92px; height: 12px; background: var(--white); border: 1px solid #c9b4aa; }
  .newsletter-btn { height: 12px; padding: 0 6px; font-size: 7px; line-height: 12px; background: #c9b4aa; color: var(--white); }
  .copyright { position: absolute; left: 159px; top: 134px; font-size: 7px; }
</style>
</head>
<body>

<header class="hero">
  <div class="hero-photo" role="img" aria-label="Close-up of a dark tufted leather sofa"></div>
  <div class="hero-tools">
    <svg width="12" height="12" viewBox="0 0 12 12" aria-label="Search"><circle cx="5" cy="5" r="3.5" fill="none" stroke="#fff" stroke-width="1.4"/><line x1="7.6" y1="7.6" x2="11" y2="11" stroke="#fff" stroke-width="1.4"/></svg>
    <svg width="12" height="12" viewBox="0 0 12 12" aria-label="Cart"><path d="M1 2h2l1.5 6h6l1-4.5H4" fill="none" stroke="#fff" stroke-width="1.2"/><circle cx="5" cy="10.5" r="1" fill="#fff"/><circle cx="10" cy="10.5" r="1" fill="#fff"/></svg>
  </div>
  <div class="hero-content">
    <p class="hero-tagline"><span class="hero-rule"></span>The Best Sofas for Less<span class="hero-rule"></span></p>
    <h1 class="brand-name">Bramwell</h1>
    <p class="brand-sub"><span class="hero-rule"></span>SOFAS SHOP<span class="hero-rule"></span></p>
    <div class="hero-actions">
      <span class="btn-pale">Browse the collection</span>
      <span class="btn-outline">Shop Now</span>
    </div>
  </div>
  <svg class="hero-down" width="10" height="6" viewBox="0 0 10 6" aria-label="Scroll down"><path d="M1 1l4 4 4-4" fill="none" stroke="#fff" stroke-width="1.4"/></svg>
</header>

<h2 class="section-title services-title">OUR SERVICES</h2>
<section class="services">
  <div class="service">
    <svg class="service-icon" viewBox="0 0 80 80" aria-label="Money bag">
      <circle cx="40" cy="40" r="38" fill="none" stroke="var(--accent)" stroke-width="1.5"/>
      <path d="M34 28h12l-3 5c8 3 11 10 11 15 0 6-6 9-14 9s-14-3-14-9c0-5 3-12 11-15z" fill="none" stroke="var(--accent)" stroke-width="1.5"/>
      <text x="40" y="51" text-anchor="middle" font-size="12" fill="var(--accent)" font-family="Raleway, sans-serif">$</text>
    </svg>
    <p class="service-text">Guaranteed lowest prices</p>
  </div>
  <div class="service">
    <svg class="service-icon" viewBox="0 0 80 80" aria-label="Delivery truck">
      <circle cx="40" cy="40" r="38" fill="none" stroke="var(--accent)" stroke-width="1.5"/>
      <path d="M20 30h26v18H20zM46 36h8l6 6v6H46z" fill="none" stroke="var(--accent)" stroke-width="1.5"/>
      <circle cx="28" cy="50" r="3" fill="var(--white)" stroke="var(--accent)" stroke-width="1.5"/>
      <circle cx="53" cy="50" r="3" fill="var(--white)" stroke="var(--accent)" stroke-width="1.5"/>
    </svg>
    <p class="service-text">Free next day delivery across the city</p>
  </div>
  <div class="service">
    <svg class="service-icon" viewBox="0 0 80 80" aria-label="Returns arrows">
      <circle cx="40" cy="40" r="38" fill="none" stroke="var(--accent)" stroke-width="1.5"/>
      <path d="M28 40a12 12 0 0 1 21-8M52 40a12 12 0 0 1-21 8" fill="none" stroke="var(--accent)" stroke-width="2"/>
      <path d="M50 26v7h-7M30 54v-7h7" fill="none" stroke="var(--accent)" stroke-width="2"/>
    </svg>
    <p class="service-text">Risk free 30 day returns on every order</p>
  </div>
</section>

<h2 class="section-title products-title">Featured Products</h2>
<section class="products">
  <article class="product">
    <div class="product-photo photo-a" role="img" aria-label="Linen loveseat in a bright room"></div>
    <div class="product-info"><span class="product-name">Linen Loveseat</span><span class="product-price">$890</span></div>
  </article>
  <article class="product">
    <div class="product-photo photo-b" role="img" aria-label="Dark grey corner chaise sofa"></div>
    <div class="product-info"><span class="product-name">Corner Chaise</span><span class="product-price">$1,240</span></div>
  </article>
  <article class="product">
    <div class="product-photo photo-c" role="img" aria-label="Grey lounge sofa beside a window"></div>
    <div class="product-info"><span class="product-name">Grey Lounge Sofa</span><span class="product-price">$1,150</span></div>
  </article>
  <article class="product">
    <div class="product-photo photo-d" role="img" aria-label="Modular sectional sofa set"></div>
    <div class="product-info"><span class="product-name">Sectional Set</span><span class="product-price">$2,380</span></div>
  </article>
</section>
<span class="view-all">View all products</span>

<footer class="site-footer">
  <div class="footer-cols">
    <div class="footer-col"><h4>Explore</h4><ul><li>Home</li><li>Sofas</li><li>About</li><li>Contact</li></ul></div>
    <div class="footer-col"><h4>Information</h4><ul><li>FAQ</li><li>Shipping</li><li>Returns</li></ul></div>
    <div class="footer-col"><h4>Support</h4><ul><li><span class="dot"></span>Help</li><li><span class="dot"></span>Orders</li><li><span class="dot"></span>Account</li></ul></div>
    <div class="footer-col"><h4>Social</h4><ul><li><span class="dot"></span>Follow</li><li><span class="dot"></span>News</li><li><span class="dot"></span>Events</li></ul></div>
  </div>
  <div class="newsletter">
    <h4>Newsletter</h4>
    <div class="newsletter-field"><span class="newsletter-input"></span><span class="newsletter-btn">Join</span></div>
  </div>
  <p class="copyright">© 2015 Bramwell Sofa Shop. Powered by Storvik</p>
</footer>

</body>
</html>
```